Funeral Services Site

We need a website for a Funeral Services company. The old website is: www.rouwcentrumkorvelaer.be We need the same structure and text.

Target Market(s)

Customers.

Coding

Coded - Design and coding required

Number of Pages Required

4 page

Font styles to use
Serif
Sans Serif
Script

```html
<!DOCTYPE html>
<html lang="en">
<head>
<meta charset="utf-8">
<title>Funeral home Korvelaer bvba</title>
<link rel="stylesheet" href="https://fonts.googleapis.com/css2?family=Cormorant+Garamond:wght@500;600&family=Open+Sans:wght@400;600&display=swap">
<style>
:root{
  --ink:#3a3a3a;
  --muted:#7a7a7a;
  --line:#d9d9d9;
  --paper:#ffffff;
  --mist:#f1f0ee;
  --bar:#4a4a4a;
  --dark:#2f2f2f;
  --stone:#8c8c8c;
}
*{box-sizing:border-box;margin:0;padding:0}
html,body{width:1200px;height:4472px;overflow:hidden}
body{font-family:"Open Sans",Arial,sans-serif;color:var(--ink);background:var(--paper);font-size:13px;line-height:1.7}
.wrap{width:1040px;margin:0 auto;position:relative}
.btn{display:inline-block;font-family:"Cormorant Garamond",Georgia,serif;font-weight:600;font-size:19px;padding:10px 26px;border:1px solid var(--ink);color:var(--ink);background:var(--paper);border-radius:3px;text-decoration:none}
.btn.light{border-color:#fff}
.section-title{font-family:"Cormorant Garamond",Georgia,serif;font-weight:600;font-size:44px;line-height:1.1;text-align:center;letter-spacing:1px;color:var(--ink)}

/* top bar */
.topbar{height:32px;background:var(--bar);color:#ddd;font-size:11px}
.topbar .wrap{display:flex;align-items:center;height:32px;gap:36px}
.topbar .login{margin-left:auto}
.topbar svg{width:11px;height:11px;vertical-align:-1px;margin-right:6px;fill:#ccc}

/* header */
.header{height:112px;background:var(--paper);box-shadow:0 2px 6px rgba(0,0,0,.08);position:relative;z-index:2}
.header .wrap{display:flex;align-items:center;height:112px}
.brand{font-family:"Cormorant Garamond",Georgia,serif;font-weight:600;font-size:24px;line-height:1.05;color:var(--ink)}
.nav{margin-left:auto;display:flex;gap:40px;font-size:13px}

/* hero */
.hero{height:496px;position:relative;background:linear-gradient(90deg,#f6f5f3 0%,#eeece8 40%,#dcdad4 70%,#c9c8bf 100%)}
.hero-photo{position:absolute;right:0;top:0;width:640px;height:496px;background:radial-gradient(circle at 55% 45%,#ffffff 0%,#e8e8e0 35%,#b9bca8 70%,#9aa08a 100%);opacity:.85}
.hero-text{position:absolute;left:80px;top:110px;width:620px}
.hero-text .pre{font-family:"Cormorant Garamond",Georgia,serif;font-size:30px;color:var(--ink)}
.hero-text h1{font-family:"Cormorant Garamond",Georgia,serif;font-weight:600;font-size:58px;line-height:1.05;margin-top:6px}
.hero-actions{margin-top:44px;display:flex;gap:20px}

/* about */
.about{height:640px;background:var(--mist);padding-top:80px}
.about-card{width:1040px;height:480px;margin:0 auto;background:var(--paper);box-shadow:0 2px 14px rgba(0,0,0,.08);display:flex;align-items:center;padding:0 48px;gap:48px}
.about-photo{width:400px;height:236px;background:linear-gradient(160deg,#8ea36d 0%,#5e6e48 45%,#7a5a48 75%,#a8a6a0 100%);flex:none}
.about-body h2{font-family:"Cormorant Garamond",Georgia,serif;font-weight:600;font-size:42px;margin-bottom:22px}
.about-body p{color:var(--muted);margin-bottom:14px;font-size:12.5px}
.about-body .btn{font-size:14px;padding:6px 16px;margin-top:10px}

/* organization */
.organization{height:800px;padding-top:190px}
.org-text{width:900px;margin:40px auto 0;text-align:center;color:var(--muted);font-size:12.5px}
.org-text p{margin-bottom:12px}
.services{width:960px;margin:70px auto 0;display:flex;justify-content:space-between}
.service{display:flex;align-items:center;gap:22px;width:300px}
.service-icon{width:64px;height:64px;border-radius:50%;background:var(--stone);flex:none;display:flex;align-items:center;justify-content:center}
.service-icon svg{width:30px;height:30px;fill:#fff}
.service p{font-family:"Cormorant Garamond",Georgia,serif;font-size:20px;line-height:1.2;text-align:center}

/* gallery */
.gallery{height:800px;position:relative;padding-top:110px;background:linear-gradient(180deg,#f3f2f0 0%,#f7f6f4 55%,#e9e8e4 100%)}
.gallery-grid{width:1000px;margin:50px auto 0;display:grid;grid-template-columns:repeat(4,226px);gap:32px 32px;justify-content:space-between}
.flower{height:184px;background:radial-gradient(circle at 50% 55%,#f4f4ee 0%,#cfd5c0 40%,#6d7a5c 75%,#4d4f48 100%)}
.gallery .more{display:block;width:170px;margin:46px auto 0;text-align:center}

/* condolences */
.condole{height:780px;padding-top:120px}
.condole-intro{width:820px;margin:26px auto 0;text-align:center;color:var(--muted);font-size:12.5px}
.cards{width:1000px;margin:44px auto 0;display:flex;justify-content:space-between}
.card{width:480px;height:330px;background:var(--mist);border:1px solid var(--line);position:relative;padding:30px 28px;display:flex;gap:24px}
.ribbon{position:absolute;right:36px;top:-6px;width:34px;height:64px;background:var(--stone);clip-path:polygon(0 0,100% 0,100% 100%,50% 78%,0 100%)}
.person{width:150px;flex:none}
.portrait{width:150px;height:150px;border-radius:50%;background:linear-gradient(160deg,#d6d2cc,#9c968e)}
.person h3{font-family:"Cormorant Garamond",Georgia,serif;font-weight:600;font-size:21px;line-height:1.1;margin-top:14px}
.person .dates{font-size:10.5px;color:var(--muted);line-height:1.4}
.person .tag{display:block;margin-top:8px;font-size:10.5px;border-bottom:1px solid var(--line)}
.condole-form{flex:1;padding-top:52px;display:flex;flex-direction:column;gap:10px}
.field{height:32px;background:var(--paper);border:1px solid var(--line);font-size:11px;color:#aaa;padding:6px 10px}
.field.tall{height:70px}
.condole-form .send{align-self:flex-end;font-size:12px;padding:4px 18px;border:1px solid var(--ink);background:var(--paper)}

/* call to action */
.cta{height:300px;position:relative;background:linear-gradient(90deg,#cfcac2 0%,#efebe4 30%,#f6f2ec 50%,#e6e0d6 70%,#bdb7ad 100%);text-align:center;padding-top:82px}
.cta h2{font-family:"Cormorant Garamond",Georgia,serif;font-weight:600;font-size:31px;line-height:1.15;width:1000px;margin:0 auto;color:#444;letter-spacing:.5px}
.cta .actions{margin-top:26px;display:flex;justify-content:center;gap:18px}

/* footer */
.footer{height:480px;background:var(--paper);padding-top:78px}
.footer .wrap{display:grid;grid-template-columns:380px 180px 220px 220px;justify-content:space-between}
.footer h4{font-family:"Cormorant Garamond",Georgia,serif;font-weight:600;font-size:20px;margin-bottom:18px}
.footer .brand{margin-bottom:18px}
.footer p,.footer li{font-size:11.5px;color:var(--muted);list-style:none;margin-bottom:10px}
.footer li svg{width:11px;height:11px;fill:var(--stone);margin-right:8px;vertical-align:-1px}
.copyright{height:32px;background:var(--mist);text-align:center;font-size:10.5px;color:var(--muted);line-height:32px}
</style>
</head>
<body>

<div class="topbar">
  <div class="wrap">
    <span><svg viewBox="0 0 12 12"><path d="M0 2h12v8H0z M0 2l6 5 6-5"/></svg>info@rouwcentrumkorvelaer.be</span>
    <span><svg viewBox="0 0 12 12"><path d="M2 0l3 3-1.5 2a7 7 0 0 0 3.5 3.5L9 7l3 3-2 2C4 12 0 8 0 2z"/></svg>011 48 27 90</span>
    <span><svg viewBox="0 0 12 12"><path d="M6 0a4 4 0 0 1 4 4c0 3-4 8-4 8S2 7 2 4a4 4 0 0 1 4-4z"/></svg>Kerkweg 14, 3795 Oudervelde</span>
    <span class="login">Login</span>
  </div>
</div>

<header class="header">
  <div class="wrap">
    <div class="brand">Funeral home<br>Korvelaer bvba</div>
    <nav class="nav"><span>Home</span><span>About us</span><span>Condole online</span><span>Order flowers</span><span>Contact</span></nav>
  </div>
</header>

<section class="hero">
  <div class="hero-photo" role="img" aria-label="White lilies and roses in a funeral arrangement"></div>
  <div class="hero-text">
    <div class="pre">Funeral home Korvelaer bvba:</div>
    <h1>A Personal Service In farewell guidance</h1>
    <div class="hero-actions"><span class="btn light">Call 011 48 27 90</span><span class="btn light">Contact Us</span></div>
  </div>
</section>

<section class="about">
  <div class="about-card">
    <div class="about-photo" role="img" aria-label="Brick funeral home building behind a willow tree"></div>
    <div class="about-body">
      <h2>ABOUT US</h2>
      <p>Rouwcentrum Korvelaer offers a complete service in mourning and farewell guidance.</p>
      <p>Funeral home Korvelaer has been a family business in the heart of the village for three generations. We take care of all practical and administrative matters, so that you can focus on your farewell.</p>
      <p>Our funeral home is a warm, quiet place where the family can say goodbye in peace. A personal and respectful farewell is our first concern.</p>
      <span class="btn">Read More</span>
    </div>
  </div>
</section>

<section class="organization">
  <h2 class="section-title">ORGANIZATION FUNERAL<br>AND WORSHIP</h2>
  <div class="org-text">
    <p>The organization of the funeral is discussed with the family in full detail. We listen to your wishes and guide you step by step, from the first call to the last farewell, with respect for every tradition.</p>
    <p>The funeral can take place in our own auditorium or in the parish church of your choice. We offer the following services:</p>
  </div>
  <div class="services">
    <div class="service"><div class="service-icon"><svg viewBox="0 0 30 30"><path d="M18 3a12 12 0 1 0 9 18A10 10 0 0 1 18 3z"/></svg></div><p>vigil the night before<br>the funeral</p></div>
    <div class="service"><div class="service-icon"><svg viewBox="0 0 30 30"><path d="M14 4v20l-6 3V14z M16 4v20l6 3V14z"/></svg></div><p>prayer service with<br>funeral possible</p></div>
    <div class="service"><div class="service-icon"><svg viewBox="0 0 30 30"><circle cx="10" cy="9" r="4"/><circle cx="20" cy="9" r="4"/><path d="M3 26c0-7 14-7 14 0z M13 26c0-7 14-7 14 0z"/></svg></div><p>Eucharistic celebration<br>with priest (on Tuesday<br>and Friday in the<br>parishes of Oudervelde)</p></div>
  </div>
</section>

<section class="gallery" aria-label="Flower arrangements">
  <h2 class="section-title">ORGANIZATION FUNERAL<br>AND WORSHIP</h2>
  <div class="gallery-grid">
    <div class="flower" role="img" aria-label="White rose coffin spray"></div>
    <div class="flower" role="img" aria-label="Long white floral arrangement"></div>
    <div class="flower" role="img" aria-label="Heart shaped white wreath"></div>
    <div class="flower" role="img" aria-label="Round white funeral bouquet"></div>
    <div class="flower" role="img" aria-label="White roses and greenery"></div>
    <div class="flower" role="img" aria-label="Low white floral piece"></div>
    <div class="flower" role="img" aria-label="Cross shaped flower arrangement"></div>
    <div class="flower" role="img" aria-label="White chrysanthemum bouquet"></div>
  </div>
  <span class="btn more">View More</span>
</section>

<section class="condole">
  <h2 class="section-title">CONDOLE ONLINE</h2>
  <p class="condole-intro">On our website you can leave a message of condolence for the family. Choose the deceased below and write a few warm words; we pass them on to the relatives.</p>
  <div class="cards">
    <article class="card">
      <span class="ribbon"></span>
      <div class="person">
        <div class="portrait" role="img" aria-label="Portrait photo of the deceased"></div>
        <h3>Maria Vandael</h3>
        <div class="dates">May 12, 1936 – Mar 4, 2019</div>
        <span class="tag">Personal funeral letter</span>
        <span class="tag">Order flowers</span>
      </div>
      <div class="condole-form">
        <div class="field">Write your name</div>
        <div class="field">Your email</div>
        <div class="field tall">Your message</div>
        <span class="send">Send</span>
      </div>
    </article>
    <article class="card">
      <span class="ribbon"></span>
      <div class="person">
        <div class="portrait" role="img" aria-label="Portrait photo of the deceased"></div>
        <h3>Frans Willem Peeters</h3>
        <div class="dates">Jan 8, 1931 – Feb 27, 2019</div>
        <span class="tag">Personal funeral letter</span>
        <span class="tag">Order flowers</span>
      </div>
      <div class="condole-form">
        <div class="field">Write your name</div>
        <div class="field">Your email</div>
        <div class="field tall">Your message</div>
        <span class="send">Send</span>
      </div>
    </article>
  </div>
</section>

<section class="cta" role="img" aria-label="Softly lit white candles">
  <h2>DO YOU HAVE ANY QUESTIONS OR WOULD YOU LIKE TO CALL<br>IN OUR FUNERAL HOME? CONTACT US. WE ARE HERE FOR YOU.</h2>
  <div class="actions"><span class="btn">Call 011 48 27 90</span><span class="btn">Contact Us</span></div>
</section>

<footer class="footer">
  <div class="wrap">
    <div>
      <div class="brand">Funeral home<br>Korvelaer bvba</div>
      <p>Funeral home Korvelaer is a family business that offers a complete and personal service in mourning and farewell guidance.</p>
      <p>We are always available, day and night, to help you with every practical question and to guide you with care.</p>
    </div>
    <div>
      <h4>Quick Link</h4>
      <ul><li>Home</li><li>About us</li><li>Condole online</li><li>Order flowers</li><li>Contact</li></ul>
    </div>
    <div>
      <h4>Our Services</h4>
      <ul><li>Vigil the night before the funeral</li><li>Prayer service with funeral</li><li>Eucharistic celebration with priest</li></ul>
    </div>
    <div>
      <h4>Our Contacts</h4>
      <ul>
        <li><svg viewBox="0 0 12 12"><path d="M6 0a4 4 0 0 1 4 4c0 3-4 8-4 8S2 7 2 4a4 4 0 0 1 4-4z"/></svg>Kerkweg 14, 3795 Oudervelde</li>
        <li><svg viewBox="0 0 12 12"><path d="M0 2h12v8H0z"/></svg>info@rouwcentrumkorvelaer.be</li>
        <li><svg viewBox="0 0 12 12"><path d="M2 0l3 3-1.5 2a7 7 0 0 0 3.5 3.5L9 7l3 3-2 2C4 12 0 8 0 2z"/></svg>011 48 27 90</li>
      </ul>
    </div>
  </div>
</footer>
<div class="copyright">Copyright 2019 Korvelaer. All Rights Reserved.</div>

</body>
</html>
```